Dredging Contractors, we run amphibious walking dredges cleaning up waterways, mines etc

We need an updated web design for our company based in Australia.
We have 20t "Walking" amphibious excavators that service mining companies and governments, cleaning up waterways and pond systems.
We would like to see designs that reflect our cutting edge marine / technology that appeals to our engineering / civil / mining clients. As well as providing benefits by cleaning up our marine waterways.
We have an existing web page at www.korvellmarine.com.au

Target Market(s)

Mining companies, engineers, council civil engineers, developers, waterways engineers

Industry/Entity Type

It Company

Requirements
Must have
• Logo, contact details, Photos of equipment page (Gallery), quotation page, Contact page, list of capabilities page (Products and services),

```html
<!DOCTYPE html>
<html lang="en">
<head>
<meta charset="utf-8">
<title>Korvell Marine – Amphibious Dredging</title>
<link rel="stylesheet" href="https://fonts.googleapis.com/css2?family=Arimo:wght@400;700&family=Jost:wght@600;700&display=swap">
<style>
  :root{
    --teal:#1aa3b3;
    --teal-deep:#0f6c7b;
    --ink:#222;
    --nav:#555;
    --band:#aadfea;
    --band-text:#176a78;
    --white:#fff;
  }
  *{box-sizing:border-box;margin:0;padding:0}
  html,body{width:1200px;height:960px;overflow:hidden;background:var(--white)}
  body{position:relative;font-family:"Arimo",Arial,sans-serif;color:var(--ink)}

  .brand{position:absolute;left:216px;top:20px;display:flex;align-items:center;gap:10px}
  .brand-dot{width:54px;height:54px;border-radius:50%;background:var(--teal)}
  .brand-name{font-family:"Jost",sans-serif;font-weight:700;font-size:22px;line-height:22px;color:var(--ink);letter-spacing:.5px}

  .hotline{position:absolute;right:216px;top:14px;font-size:10px;color:var(--teal)}
  .social{position:absolute;left:910px;top:32px;display:flex;gap:4px}
  .social span{width:35px;height:35px;border-radius:50%;background:var(--teal);display:block}

  .main-nav{position:absolute;left:0;top:98px;width:1200px;text-align:center;font-size:11.6px;line-height:24px;color:var(--nav)}
  .main-nav a{color:inherit;text-decoration:none;margin:0 6px}

  .hero{position:absolute;left:0;top:170px;width:1200px;height:392px;
    background:linear-gradient(180deg,#66c2cf 0%,#8ad1dc 40%,#1d5a67 62%,#3a9fb0 72%,#6fc7d4 100%)}
  .hero-side{position:absolute;left:0;top:0;width:421px;height:392px}
  .panel-title{position:absolute;left:216px;top:16px;font-family:"Jost",sans-serif;font-weight:700;font-size:13.5px;color:var(--white);letter-spacing:.4px}
  .service-list{position:absolute;left:216px;top:40px;list-style:none;font-size:10px;font-weight:700;line-height:19.2px;color:var(--teal-deep)}
  .cta{position:absolute;left:217px;top:329px;width:167px;height:46px;background:var(--teal);color:var(--white);
    font-family:"Jost",sans-serif;font-weight:700;font-size:14px;line-height:46px;text-align:center;letter-spacing:.4px}
  .hero-photo{position:absolute;left:421px;top:0;width:563px;height:392px;
    background:linear-gradient(180deg,#3d8fe0 0%,#7ab8ef 55%,#3f7a44 80%,#2f6b3a 100%)}
  .dots{position:absolute;right:12px;top:14px;display:flex;gap:4px}
  .dots i{width:7.2px;height:7.2px;border-radius:50%;background:var(--white);display:block}
  .dots i.on{background:var(--teal)}

  .info{position:absolute;left:0;top:562px;width:1200px;height:274px;background:var(--band)}
  .info h2{position:absolute;top:36px;font-family:"Jost",sans-serif;font-weight:700;font-size:14px;color:var(--teal-deep);letter-spacing:.4px}
  .company h2{left:213px}
  .company p{position:absolute;left:216px;width:334px;font-size:14.2px;line-height:19.2px;color:var(--band-text);text-align:justify}
  .apps h2{left:584px}
  .apps ul{position:absolute;left:584px;top:68px;width:362px;list-style:none;font-size:9.6px;line-height:14.4px;color:var(--band-text)}
  .apps li{position:relative;padding-left:11px;text-align:justify}
  .apps li::before{content:"";position:absolute;left:0;top:3px;width:6px;height:6px;border-radius:50%;background:var(--white)}

  .legal{position:absolute;left:0;top:849px;width:1200px;text-align:center;font-size:8px;color:var(--teal-deep)}
  .foot-brand{position:absolute;left:220px;top:884px;display:flex;align-items:center;gap:6px}
  .foot-brand .brand-dot{width:32px;height:32px;background:#888}
  .foot-brand .brand-name{font-size:13px;line-height:13px;color:#444}
  .foot-nav{position:absolute;left:380px;top:884px;width:440px;text-align:center;font-size:6.4px;line-height:14.4px;color:#444}
  .foot-nav a{color:inherit;text-decoration:none;margin:0 3px}
</style>
</head>
<body>
  <header>
    <div class="brand"><span class="brand-dot"></span><span class="brand-name">KORVELL<br>MARINE</span></div>
    <p class="hotline">Cutter Suction, Excavator Bucket, Weed Rake PH 1300 KORVEL (567835)</p>
    <div class="social" aria-label="Social links"><span></span><span></span></div>
    <nav class="main-nav">
      <div><a>HOME</a><a>QUOTATION / EVALUATION FORM</a><a>CUTTER SUCTION</a><a>DREDGE SLURRY SEPARATION SYSTEM</a><a>AMPHIBIOUS EXCAVATOR</a></div>
      <div><a>AQUATIC WEED MANAGEMENT</a><a>DEWATERING GEO TEXTILE TUBES</a><a>FLOOD CONTROL - CREEK &amp; RIVER CLEARING</a><a>MOBILITY</a></div>
      <div><a>CAPABILITIES</a><a>SPYDER EXCAVATOR</a><a>PREVIOUS DREDGING WORK</a><a>PICTURE GALLERY</a><a>CONTACT US</a></div>
    </nav>
  </header>

  <section class="hero">
    <div class="hero-side">
      <h2 class="panel-title">PRODUCTS &amp; SERVICES</h2>
      <ul class="service-list">
        <li>TAILINGS DAMS / PUMP INLETS / OUTLETS</li>
        <li>RIVERS / CREEKS / PONDS</li>
        <li>BOAT / CHANNEL PASSAGE</li>
        <li>AQUATIC WEED MANAGEMENT</li>
        <li>CIVIL ENGINEERING</li>
        <li>FLOOD CONTROL - CREEK CLEARING</li>
        <li>LINKS</li>
        <li>NEWSLETTER</li>
        <li>DREDGING VIDEOS</li>
        <li>CONTACT DETAILS</li>
      </ul>
      <div class="cta">CONTACT NOW</div>
    </div>
    <div class="hero-photo" role="img" aria-label="Green amphibious excavator dredge lifted by a crane against a blue sky">
      <div class="dots"><i></i><i></i><i></i><i></i><i></i><i></i><i></i><i></i><i></i><i class="on"></i><i></i><i></i></div>
    </div>
  </section>

  <section class="info">
    <div class="company">
      <h2>COMPANY INFORMATION</h2>
      <p style="top:74px">Korvell Marine has been working as waterways engineers since 1995.</p>
      <p style="top:122px">Our amphibious dredges are highly mobile and is easily transported by truck to anywhere in Australia.</p>
      <p style="top:170px;text-align:left">Our portable dewatering systems enable us to pump straight from the dregde and dry material down to 25 microns.</p>
    </div>
    <div class="apps">
      <h2>IDEAL APPLICATIONS FOR OUR MULTIPURPOSE DREDGER</h2>
      <ul>
        <li>Suction and backhoe dredging in rivers, canals, harbours, lakes and coastal waters.</li>
        <li>Amphibious Dredging in areas where it is difficult or impossible to work with other machinery (wetlands, shallow waters, shorelines, industrial pools, under bridges, in tunnels, etc).</li>
        <li style="text-align:left">Where a versatile dredger is needed, which can both pump and excavate.</li>
        <li>Where it is not feasible to mobilise several single-purpose machines (cutter-suction dredger, backhoe dredger, tugboat, assembly cranes).</li>
        <li style="text-align:left">Where pile driving in water or on the shoreline is needed.</li>
        <li style="text-align:left">Where vegetation disturbs conventional dredgers.</li>
        <li style="text-align:left">Where vegetation needs to be removed.</li>
        <li style="text-align:left">Environmental dredging.</li>
      </ul>
    </div>
  </section>

  <footer>
    <p class="legal">Ph: 1300 567 835 (Korvel) Email: info@korvellmarine.com.au Copyright © 2009, Rhys Calder -Korvell Marine. All rights reserved.</p>
    <div class="foot-brand"><span class="brand-dot"></span><span class="brand-name">KORVELL<br>MARINE</span></div>
    <nav class="foot-nav">
      <div><a>HOME</a><a>QUOTATION / EVALUATION FORM</a><a>CUTTER SUCTION</a><a>DREDGE SLURRY SEPARATION SYSTEM</a><a>AMPHIBIOUS EXCAVATOR</a></div>
      <div><a>AQUATIC WEED MANAGEMENT</a><a>DEWATERING GEO TEXTILE TUBES</a><a>FLOOD CONTROL - CREEK &amp; RIVER CLEARING</a><a>MOBILITY</a></div>
      <div><a>CAPABILITIES</a><a>SPYDER EXCAVATOR</a><a>PREVIOUS DREDGING WORK</a><a>PICTURE GALLERY</a><a>CONTACT US</a></div>
    </nav>
  </footer>
</body>
</html>
```